Flyer design for mental health and disability support work company.

The company name 'Marlow Disability'

we need a flyer design for our company.

Specialising
Marlow Disability is a new RFTQ service aimed towards RFTQ participants with psychosocial/mental health, intellectual, and cognitive disabilities. We also specialise in supporting participants with a history of being involved in the criminal justice system.

Our focus
Focusing on providing core RFTQ supports for community participation, daily activities and supported independent living.

Authentic
Like-minded people passionate about wanting to make a difference in participants' lives.

Our aim is to provide holistic and empowering support targeted towards creating independence and guidance for all participants and families.

Over 35 years of experience working with people with a vast range of disabilities and individual support needs.

Extensive experience not only within RFTQ but working with mainstream services within Ulmera Justice, Health, Corrections and Parole, Housing, Keystep Hub, Paywarden, Lawbridge, PMTQ and NSW court systems.

website www.marlowdisability.com.au
email for referrals send to - referrals@marlowdisability.com.au
for further information send to - hello@marlowdisability.com.au

number 1800 372 519

Font styles to use
Serif

Requirements
Should not have
• pictures with people that have disabilities

```html
<!DOCTYPE html>
<html lang="en">
<head>
<meta charset="utf-8">
<title>Marlow Disability Flyer</title>
<link rel="stylesheet" href="https://fonts.googleapis.com/css2?family=Poppins:wght@400;500;600;700&family=Oswald:wght@500;600&display=swap">
<style>
  :root {
    --navy: #173761;
    --navy-deep: #122d52;
    --sky: #79b6ea;
    --gold: #f1b722;
    --gold-mid: #f1cf73;
    --gold-light: #f3dfae;
    --ink: #1c2f4c;
    --white: #ffffff;
    --backdrop: #dedede;
  }
  * { margin: 0; padding: 0; box-sizing: border-box; }
  html, body { width: 1200px; height: 2496px; overflow: hidden; }
  body { background: var(--backdrop); font-family: "Poppins", sans-serif; color: var(--ink); position: relative; }
  .flyer { position: absolute; left: 37px; top: 453px; width: 1125px; height: 1590px; background: var(--white); overflow: hidden; box-shadow: 0 10px 24px rgba(0,0,0,.25); }
  .abs { position: absolute; }

  .hero-band { left: 0; top: 135px; width: 1125px; height: 555px; background: var(--navy); }
  .hero-photo { left: 360px; top: 135px; width: 765px; height: 555px;
    background: linear-gradient(90deg, rgba(23,55,97,1) 0%, rgba(70,80,70,.9) 30%, #b48c2a 62%, #f0b81c 85%, #f6c21e 100%); }

  .logo { left: 84px; top: 49px; width: 186px; height: 186px; border-radius: 50%; background: var(--navy); border: 5px solid var(--white); box-shadow: 0 0 0 3px var(--sky);
    display: flex; align-items: center; justify-content: center; }
  .logo-name { color: var(--white); font-weight: 600; font-size: 22px; letter-spacing: 1px; }

  .headline { left: 85px; top: 265px; color: var(--white); font-weight: 700; font-size: 49px; line-height: 53px; text-transform: uppercase; }
  .headline .light { font-weight: 400; color: var(--sky); }
  .headline .accent { color: var(--sky); }
  .rule { left: 85px; top: 432px; width: 48px; height: 5px; background: var(--gold); border-radius: 3px; }

  .section-title { font-size: 30px; font-weight: 400; text-transform: uppercase; line-height: 1; }
  .section-title b { font-weight: 700; color: var(--gold); }
  .spec-title { left: 85px; top: 460px; color: var(--white); }
  .spec-intro { left: 85px; top: 503px; width: 600px; color: var(--white); font-size: 16px; line-height: 19px; }
  .check-list { list-style: none; }
  .check-list li { display: flex; align-items: flex-start; gap: 6px; }
  .check-list svg { flex: none; margin-top: 3px; }
  .spec-list { top: 550px; color: var(--white); font-size: 21px; font-weight: 600; line-height: 30px; }
  .spec-list.col-a { left: 85px; }
  .spec-list.col-b { left: 440px; }

  .focus { left: 0; top: 660px; width: 428px; }
  .focus-block { position: relative; display: flex; align-items: center; gap: 18px; padding-left: 78px; padding-right: 20px; }
  .focus-block.primary { height: 202px; background: var(--gold); border-radius: 0 24px 0 0; align-items: flex-end; padding-bottom: 36px; }
  .focus-block.second { height: 146px; background: var(--gold-mid); }
  .focus-block.third { height: 154px; background: var(--gold-light); border-radius: 0 0 24px 0; }
  .focus-title { position: absolute; left: 80px; top: 40px; color: var(--navy); }
  .focus-title b { color: var(--white); }
  .icon-badge { flex: none; width: 64px; height: 64px; border-radius: 50%; background: var(--white); border: 3px solid var(--navy); display: flex; align-items: center; justify-content: center; }
  .focus-text { font-size: 19px; font-weight: 600; line-height: 22px; color: var(--navy-deep); }

  .aim-title { left: 470px; top: 740px; display: flex; align-items: center; gap: 8px; color: var(--navy); }
  .aim-text { left: 470px; top: 790px; width: 600px; font-size: 18px; line-height: 22px; }

  .over { left: 468px; top: 884px; font-size: 40px; font-weight: 700; color: var(--navy); line-height: 48px; }
  .exp-frame { left: 580px; top: 922px; width: 480px; height: 232px; border: 2px solid var(--navy); border-left: none; border-radius: 0 30px 30px 0; }
  .exp-base { left: 470px; top: 1153px; width: 112px; height: 2px; background: var(--navy); }
  .exp-dot { left: 466px; top: 1149px; width: 10px; height: 10px; border-radius: 50%; background: var(--navy); }
  .exp-badge { left: 640px; top: 948px; width: 395px; height: 118px; background: var(--gold); border-radius: 6px 14px 14px 6px; }
  .years-of { left: 672px; top: 952px; font-size: 28px; font-weight: 500; color: var(--navy); line-height: 36px; }
  .experience { left: 672px; top: 982px; font-family: "Oswald", sans-serif; font-size: 66px; font-weight: 600; color: var(--white); line-height: 80px; white-space: nowrap; }
  .big-35 { left: 462px; top: 938px; font-size: 150px; font-weight: 700; color: var(--navy); letter-spacing: -8px; line-height: 1; }
  .exp-caption { left: 472px; top: 1083px; width: 570px; font-size: 18px; line-height: 22px; }

  .authentic-seal { left: 82px; top: 1243px; width: 136px; height: 136px; border-radius: 50%; background: var(--white); border: 8px solid var(--navy); box-shadow: inset 0 0 0 10px var(--gold); }
  .authentic-text { left: 233px; top: 1243px; width: 170px; font-size: 19px; font-weight: 600; color: var(--navy); line-height: 23px; }
  .divider { top: 1220px; width: 1px; height: 150px; background: #c9ced6; }

  .work-title { left: 470px; top: 1232px; color: var(--navy); }
  .work-list { top: 1290px; font-size: 16px; line-height: 20px; color: var(--ink); }
  .work-list li { margin-bottom: 10px; }

  .footer { left: 0; top: 1470px; width: 1125px; height: 120px; background: var(--navy); }
  .contact { left: 105px; top: 1496px; color: var(--white); font-size: 19px; line-height: 26px; }
  .contact li { display: flex; align-items: center; gap: 6px; }
  .web-bar { left: 470px; top: 1455px; width: 655px; height: 74px; background: var(--gold); border-radius: 12px 0 0 0;
    display: flex; align-items: center; justify-content: center; font-size: 30px; font-weight: 600; letter-spacing: 3px; color: var(--navy); }
  .web-bar b { color: var(--white); font-weight: 700; }
</style>
</head>
<body>
<main class="flyer">
  <div class="abs hero-band"></div>
  <div class="abs hero-photo" role="img" aria-label="Golden sunset over calm shoreline water"></div>

  <div class="abs logo"><span class="logo-name">MARLOW</span></div>

  <h1 class="abs headline"><span class="accent">Expert</span> <span class="light">in</span><br>Mental Health <span class="light">&amp;</span><br>Disability Support</h1>
  <div class="abs rule"></div>

  <h2 class="abs section-title spec-title">Specializing <b>in</b></h2>
  <p class="abs spec-intro">Marlow Disability is a new RFTQ service aimed toward RFTQ participants with a history of</p>
  <ul class="abs check-list spec-list col-a">
    <li><svg width="16" height="16" viewBox="0 0 16 16"><rect x="1" y="2" width="12" height="12" fill="none" stroke="#79b6ea" stroke-width="1.6"/><path d="M3.5 8l3 3 7-8" fill="none" stroke="#79b6ea" stroke-width="2"/></svg>Criminal justice</li>
    <li><svg width="16" height="16" viewBox="0 0 16 16"><rect x="1" y="2" width="12" height="12" fill="none" stroke="#79b6ea" stroke-width="1.6"/><path d="M3.5 8l3 3 7-8" fill="none" stroke="#79b6ea" stroke-width="2"/></svg>Psychosocial/mental health</li>
  </ul>
  <ul class="abs check-list spec-list col-b">
    <li><svg width="16" height="16" viewBox="0 0 16 16"><rect x="1" y="2" width="12" height="12" fill="none" stroke="#79b6ea" stroke-width="1.6"/><path d="M3.5 8l3 3 7-8" fill="none" stroke="#79b6ea" stroke-width="2"/></svg>Intellectual</li>
    <li><svg width="16" height="16" viewBox="0 0 16 16"><rect x="1" y="2" width="12" height="12" fill="none" stroke="#79b6ea" stroke-width="1.6"/><path d="M3.5 8l3 3 7-8" fill="none" stroke="#79b6ea" stroke-width="2"/></svg>Cognitive disabilities</li>
  </ul>

  <section class="abs focus">
    <div class="focus-block primary">
      <h2 class="section-title focus-title">Our <b>Focus</b></h2>
      <span class="icon-badge"><svg width="36" height="30" viewBox="0 0 36 30"><circle cx="18" cy="8" r="5" fill="#173761"/><circle cx="7" cy="11" r="4" fill="#173761"/><circle cx="29" cy="11" r="4" fill="#173761"/><path d="M9 28c0-7 4-12 9-12s9 5 9 12z" fill="#173761"/><path d="M0 27c0-5 3-9 7-9 2 0 3 1 4 2-2 2-3 4-3 7z M36 27c0-5-3-9-7-9-2 0-3 1-4 2 2 2 3 4 3 7z" fill="#173761"/></svg></span>
      <p class="focus-text">Focusing on providing core RFTQ supports for community participation</p>
    </div>
    <div class="focus-block second">
      <span class="icon-badge"><svg width="30" height="34" viewBox="0 0 30 34"><circle cx="15" cy="5" r="4" fill="#173761"/><path d="M2 11l13 3 13-3M15 14v8l-6 11M15 22l6 11" fill="none" stroke="#173761" stroke-width="3.5" stroke-linecap="round"/></svg></span>
      <p class="focus-text">Daily<br>activities</p>
    </div>
    <div class="focus-block third">
      <span class="icon-badge"><svg width="30" height="32" viewBox="0 0 30 32"><path d="M15 3L3 13h4v16h16V13h4z" fill="#173761"/><rect x="12" y="19" width="6" height="10" fill="#fff"/></svg></span>
      <p class="focus-text">Supported<br>independent<br>living</p>
    </div>
  </section>

  <h2 class="abs section-title aim-title"><svg width="36" height="36" viewBox="0 0 36 36"><circle cx="18" cy="18" r="15" fill="none" stroke="#173761" stroke-width="3.5"/><circle cx="18" cy="18" r="8" fill="none" stroke="#173761" stroke-width="3"/><circle cx="18" cy="18" r="2.5" fill="#173761"/><path d="M18 18L32 4" stroke="#f1b722" stroke-width="3"/></svg>Our <b>Aim</b></h2>
  <p class="abs aim-text">to provide holistic and empowering supports targeted towards creating independence and guidance for all participants and families.</p>

  <div class="abs exp-frame"></div>
  <div class="abs exp-base"></div>
  <div class="abs exp-dot"></div>
  <p class="abs over">OVER</p>
  <div class="abs exp-badge"></div>
  <p class="abs years-of">YEARS OF</p>
  <p class="abs experience">EXPERIENCE</p>
  <p class="abs big-35">35</p>
  <p class="abs exp-caption">Working with people that have psychosocial, intellectual, and cognitive disabilities</p>

  <div class="abs authentic-seal" aria-hidden="true"></div>
  <p class="abs authentic-text">Likeminded people wanting to make a difference in participant's lives.</p>
  <div class="abs divider" style="left:412px"></div>

  <h2 class="abs section-title work-title">Experienced in <b>working with</b></h2>
  <ul class="abs check-list work-list" style="left:470px">
    <li><svg width="14" height="14" viewBox="0 0 16 16"><rect x="1" y="2" width="12" height="12" fill="none" stroke="#f1b722" stroke-width="1.6"/><path d="M3.5 8l3 3 7-8" fill="none" stroke="#f1b722" stroke-width="2"/></svg>Mainstream<br>supports under</li>
    <li><svg width="14" height="14" viewBox="0 0 16 16"><rect x="1" y="2" width="12" height="12" fill="none" stroke="#f1b722" stroke-width="1.6"/><path d="M3.5 8l3 3 7-8" fill="none" stroke="#f1b722" stroke-width="2"/></svg>Justice</li>
    <li><svg width="14" height="14" viewBox="0 0 16 16"><rect x="1" y="2" width="12" height="12" fill="none" stroke="#f1b722" stroke-width="1.6"/><path d="M3.5 8l3 3 7-8" fill="none" stroke="#f1b722" stroke-width="2"/></svg>Ulmera Health</li>
  </ul>
  <div class="abs divider" style="left:672px; top:1285px; height:90px"></div>
  <ul class="abs check-list work-list" style="left:695px">
    <li><svg width="14" height="14" viewBox="0 0 16 16"><rect x="1" y="2" width="12" height="12" fill="none" stroke="#f1b722" stroke-width="1.6"/><path d="M3.5 8l3 3 7-8" fill="none" stroke="#f1b722" stroke-width="2"/></svg>Corrections</li>
    <li><svg width="14" height="14" viewBox="0 0 16 16"><rect x="1" y="2" width="12" height="12" fill="none" stroke="#f1b722" stroke-width="1.6"/><path d="M3.5 8l3 3 7-8" fill="none" stroke="#f1b722" stroke-width="2"/></svg>Housing</li>
    <li><svg width="14" height="14" viewBox="0 0 16 16"><rect x="1" y="2" width="12" height="12" fill="none" stroke="#f1b722" stroke-width="1.6"/><path d="M3.5 8l3 3 7-8" fill="none" stroke="#f1b722" stroke-width="2"/></svg>Keystep Hub</li>
  </ul>
  <div class="abs divider" style="left:872px; top:1285px; height:90px"></div>
  <ul class="abs check-list work-list" style="left:893px">
    <li><svg width="14" height="14" viewBox="0 0 16 16"><rect x="1" y="2" width="12" height="12" fill="none" stroke="#f1b722" stroke-width="1.6"/><path d="M3.5 8l3 3 7-8" fill="none" stroke="#f1b722" stroke-width="2"/></svg>Paywarden</li>
    <li><svg width="14" height="14" viewBox="0 0 16 16"><rect x="1" y="2" width="12" height="12" fill="none" stroke="#f1b722" stroke-width="1.6"/><path d="M3.5 8l3 3 7-8" fill="none" stroke="#f1b722" stroke-width="2"/></svg>Lawbridge and<br>Court processes</li>
  </ul>

  <div class="abs footer"></div>
  <ul class="abs check-list contact">
    <li><svg width="14" height="14" viewBox="0 0 16 16"><path d="M3 1l3 3-2 2c1 2 3 4 5 5l2-2 3 3-2 3C7 15 1 9 1 3z" fill="#f1b722"/></svg>1800 372 519</li>
    <li><svg width="14" height="12" viewBox="0 0 16 12"><rect x="0" y="0" width="16" height="12" fill="#f1b722"/><path d="M0 0l8 6 8-6" fill="none" stroke="#173761" stroke-width="1.4"/></svg>hello@marlowdisability.com.au</li>
  </ul>
  <div class="abs web-bar">www.<b>marlowdisability</b>.com.au</div>
</main>
</body>
</html>
```